Business Card for Pottery and Jewellery Designer

A new business card design is needed to accompany a newly launching pottery and jewellery website. The company logo has been attached for use. The company is called Glazewick Studio. For a sense of the vibe please see the website (it is currently under construction but this way you'll get a feel for the style) www.GlazewickStudio.com

The website font is Pontano Sans for the body of the text with Overlock for headers.

The overall look should be clean and elegant. The back side can have just the logo. The front side should have a smaller logo and the following details displayed:

Glazewick Studio
Designer: Hollis Marrow
Phone: xxx.xxx.xxxx
Email: Designer@GlazewickStudio.com

The structure of displaying this is completely up to you. Different layouts and creative methods of displaying contact info are welcome as long as it stays clean/uncluttered.

No product photographs are to be included in the design as the catalogue changes quickly.

Colour preferences lean towards elegant and understated (charcoal grey, dark navy blue etc.)

Please let me know if you have any further questions or further details required.

Target Market(s)

Target market is 30+ year old women

Industry/Entity Type

Construction

Colors
ffffff
1b1b1b
474747
d9d9d9
fafafa
0355a3

Requirements
Must have
• The submissions so far have looked very typical and don't stand out right now. They're also all in navy with very little variation. I'm looking for something that stands out a it more while still being clean-looking.
Nice to have
• I've attached a few design samples and an idea for a backdrop. It would be great to see some designs in black, white, and grey with only a hint of color.
Should not have
• Product Images

```html
<!DOCTYPE html>
<html lang="en">
<head>
<meta charset="utf-8">
<title>Glazewick Studio – Business Card</title>
<link rel="stylesheet" href="https://fonts.googleapis.com/css2?family=Lato:wght@400;700&display=swap">
<style>
  :root {
    --backdrop: #e9e6e2;
    --card-black: #1b1b1b;
    --card-edge: #111111;
    --stone: #dcd8d0;
    --stone-line: #474747;
    --ink: #1b1b1b;
    --text-light: #e6e6e6;
    --text-muted: #9a9a9a;
    --rule: #5a5a5a;
  }
  * { margin: 0; padding: 0; box-sizing: border-box; }
  html, body {
    width: 1200px; height: 1000px; overflow: hidden;
    background: var(--backdrop);
    font-family: "Lato", sans-serif;
  }
  .sheet {
    position: relative; width: 1200px; height: 1000px;
  }
  .card {
    position: absolute; left: 300px; width: 600px; height: 343px;
    background: var(--card-black);
    border-radius: 4px;
    overflow: hidden;
    box-shadow: 0 10px 30px rgba(0,0,0,0.18);
  }
  .card--back { top: 117px; }
  .card--front { top: 540px; }

  /* Back side */
  .back-band {
    position: absolute; left: 26px; top: 24px; width: 440px; height: 100px;
    background: var(--stone);
    border: 2px solid var(--stone-line);
    outline: 4px solid var(--stone);
    display: flex; align-items: center; gap: 18px;
    padding-left: 22px;
  }
  .brand-dot {
    width: 52px; height: 52px; border-radius: 50%;
    background: var(--stone-line); flex: none;
  }
  .brand-name {
    font-family: "Lato", sans-serif;
    font-weight: 400;
    text-transform: uppercase;
    color: var(--ink);
    letter-spacing: 0.5px;
  }
  .back-band .brand-name { font-size: 25px; }

  /* Front side */
  .front-head {
    position: absolute; left: 0; top: 0; width: 100%; height: 122px;
    background: var(--stone);
    display: flex; align-items: center; gap: 16px;
    padding-left: 34px;
  }
  .front-head .brand-dot { width: 48px; height: 48px; }
  .front-head .brand-name { font-size: 22px; }
  .front-body {
    position: absolute; left: 0; top: 122px; width: 100%; height: 221px;
    padding: 22px 34px 0 100px;
    color: var(--text-light);
  }
  .role { font-size: 14px; color: var(--text-muted); }
  .person { font-size: 19px; margin-top: 3px; }
  .rule { height: 1px; background: var(--rule); margin: 10px 0 22px; width: 420px; }
  .contact { list-style: none; font-size: 14px; color: var(--text-muted); }
  .contact li { display: flex; align-items: center; gap: 12px; margin-bottom: 10px; }
  .contact svg { width: 14px; height: 14px; fill: var(--text-light); flex: none; }
</style>
</head>
<body>
<main class="sheet">
  <section class="card card--back" aria-label="Card back">
    <div class="back-band">
      <span class="brand-dot"></span>
      <span class="brand-name">Glazewick Studio</span>
    </div>
  </section>

  <section class="card card--front" aria-label="Card front">
    <header class="front-head">
      <span class="brand-dot"></span>
      <span class="brand-name">Glazewick Studio</span>
    </header>
    <div class="front-body">
      <p class="role">Designer</p>
      <p class="person">Hollis Marrow</p>
      <div class="rule"></div>
      <ul class="contact">
        <li>
          <svg viewBox="0 0 24 24" aria-hidden="true"><path d="M6.6 10.8a15.5 15.5 0 0 0 6.6 6.6l2.2-2.2a1 1 0 0 1 1-.25 11.4 11.4 0 0 0 3.6.57 1 1 0 0 1 1 1V20a1 1 0 0 1-1 1A17 17 0 0 1 3 4a1 1 0 0 1 1-1h3.5a1 1 0 0 1 1 1c0 1.25.2 2.45.57 3.57a1 1 0 0 1-.25 1z"/></svg>
          <span>xxx.xxx.xxxx</span>
        </li>
        <li>
          <svg viewBox="0 0 24 24" aria-hidden="true"><path d="M2 5h20v14H2z M4 7v.5l8 5 8-5V7l-8 5z" fill-rule="evenodd"/></svg>
          <span>Designer@GlazewickStudio.com</span>
        </li>
      </ul>
    </div>
  </section>
</main>
</body>
</html>
```